*YO!!! Designers Needed!!* Front Page Cover Needed for a $$Billion Dollar$$ Company

We are a manufacturer of aluminum electrolytic capacitors. We are looking to create a front page cover that will be used on our annual report. We are a publicly listed company and work with many Pinnacle 300 companies, so your work will be viewed by the BIG GUNS and EXECUTIVES around the WORLD! If selected, you may be selected for additional work.

The front page cover should be unique. If elegance, modern, bling, and creativity somehow got together and had a child, that's what the cover page would look like!

Inspired Examples attached. Check them out!

www.velmoro.com

Font styles to use
Sans Serif

Requirements
Must have
• 1. Must include the attached logo. Logo size, color, and placement are at your discretion.

2. Should include the text, '2020 Annual Report'

3. The design should incorporate the use of foil and/or be embossed. The foil can be part of the design or can be the full page. See various examples attached for reference.

4. Shall be in A4 size and vertical orientation.
Nice to have
• Feel free to add any icons or stock photos (for example capacitors or circuit boards) if needed.

Be creative here and don't be afraid to be bold! The end product will be printed and budget is not a limiting factor, so feel free to make it extravagant if needed.

Our slogan is "Think Ahead". This slogan can or cannot be part of the theme.

```html
<!DOCTYPE html>
<html lang="en">
<head>
<meta charset="utf-8">
<title>Velmoro 2020 Annual Report Cover</title>
<link href="https://fonts.googleapis.com/css2?family=Oswald:wght@400;500&display=swap" rel="stylesheet">
<style>
  :root {
    --stage: #e9eeee;
    --ink: #000000;
    --photo-light: #8a8a8a;
    --photo-mid: #4e4e4e;
    --photo-low: #2a2a2a;
    --photo-dark: #101010;
    --teal: #17a88a;
    --teal-deep: #0b7a62;
    --teal-bright: #2cc3a1;
    --teal-band: #5a9a8b;
    --white: #f4f4f4;
  }
  * { margin: 0; padding: 0; box-sizing: border-box; }
  html, body {
    width: 1200px;
    height: 900px;
    overflow: hidden;
    background: var(--stage);
    font-family: "Oswald", "Arial Narrow", sans-serif;
  }
  .cover {
    position: absolute;
    left: 310px;
    top: 40px;
    width: 580px;
    height: 820px;
    background: var(--ink);
    overflow: hidden;
    box-shadow: 0 10px 30px rgba(0,0,0,0.25);
  }
  .cover__photo {
    position: absolute;
    left: 0;
    top: 150px;
    width: 100%;
    height: 600px;
    background:
      radial-gradient(ellipse 170px 120px at 74% 26%, rgba(150,150,150,0.55) 0%, rgba(90,90,90,0.25) 55%, transparent 100%),
      radial-gradient(ellipse 220px 150px at 86% 52%, rgba(170,170,170,0.6) 0%, rgba(100,100,100,0.3) 50%, transparent 100%),
      radial-gradient(ellipse 200px 110px at 56% 68%, rgba(140,140,140,0.5) 0%, rgba(80,80,80,0.25) 55%, transparent 100%),
      radial-gradient(ellipse 120px 260px at 8% 50%, rgba(60,60,60,0.5) 0%, transparent 100%),
      radial-gradient(ellipse at 62% 50%, var(--photo-low) 0%, #1a1a1a 55%, var(--photo-dark) 85%),
      linear-gradient(180deg, var(--ink) 0%, transparent 12%, transparent 80%, var(--ink) 100%);
    background-blend-mode: screen, screen, screen, screen, normal, normal;
  }
  .cover__photo::after {
    content: "";
    position: absolute;
    inset: 0;
    background: linear-gradient(180deg, var(--ink) 0%, rgba(0,0,0,0) 14%, rgba(0,0,0,0) 78%, var(--ink) 100%);
  }
  .brand {
    position: absolute;
    right: 40px;
    top: 70px;
    display: flex;
    align-items: center;
    gap: 10px;
    color: var(--white);
    font-weight: 500;
    font-size: 40px;
    letter-spacing: 1px;
    line-height: 1;
  }
  .brand__dot {
    width: 12px;
    height: 12px;
    border-radius: 50%;
    background: var(--white);
  }
  .cover__foil {
    position: absolute;
    left: 0;
    top: 520px;
    width: 370px;
    height: 300px;
  }
  .title {
    position: absolute;
    right: 40px;
    top: 545px;
    text-align: right;
    text-transform: uppercase;
    line-height: 1;
  }
  .title__year {
    display: block;
    margin-right: 36px;
    color: var(--teal);
    font-size: 80px;
    font-weight: 500;
    letter-spacing: 5px;
  }
  .title__label {
    display: block;
    margin-top: 10px;
    color: var(--white);
    font-size: 58px;
    font-weight: 400;
    letter-spacing: 3px;
  }
</style>
</head>
<body>
  <main class="cover">
    <div class="cover__photo" role="img" aria-label="Black and white photo of business people's hands with pens reviewing printed charts on a desk"></div>

    <div class="brand">
      <span class="brand__dot"></span>
      <span class="brand__name">Velmoro</span>
    </div>

    <svg class="cover__foil" viewBox="0 0 370 300">
      <defs>
        <linearGradient id="foilTone" x1="0" y1="0" x2="1" y2="1">
          <stop offset="0" stop-color="#0b7a62"/>
          <stop offset="0.18" stop-color="#2cc3a1"/>
          <stop offset="0.32" stop-color="#bfeee2"/>
          <stop offset="0.46" stop-color="#1aa988"/>
          <stop offset="0.62" stop-color="#0b7a62"/>
          <stop offset="0.78" stop-color="#9fe0cf"/>
          <stop offset="1" stop-color="#138f73"/>
        </linearGradient>
      </defs>
      <polygon points="0,0 370,0 0,300" fill="var(--teal-band)" opacity="0.8"/>
      <polygon points="0,16 330,16 0,282" fill="url(#foilTone)" role="img" aria-label="Green metallic foil panel with white triangle pattern"/>
    </svg>

    <h1 class="title">
      <span class="title__year">2020</span>
      <span class="title__label">Annual Report</span>
    </h1>
  </main>
</body>
</html>
```